Law Firm Stationery Design - Traditional Meets Intuitive

Looking for a modern, yet classic, law firm stationery design. Simplicity is desired, but great ideas are encouraged. See attachment for company information. We utilize a variety of non-traditional legal tools to bring a different perspective to each of our client's particular situation. Final design should communicate classic values with intuitive, unique solutions.

Industry/Entity Type

Law Firm

Requirements
Should not have
• - No typical legal icons
• - No Tag Line!
• - DO NOT WANT WHAT WE ALREADY HAVE

```html
<!DOCTYPE html>
<html lang="en">
<head>
<meta charset="utf-8">
<title>Veridane Law LLC – Stationery</title>
<link rel="stylesheet" href="https://fonts.googleapis.com/css2?family=Montserrat:wght@300;400;600&display=swap">
<style>
  :root {
    --teal: #02506a;
    --teal-dark: #014860;
    --backdrop: #d1d1d1;
    --paper: #f0f0f0;
    --bar-grey: #959595;
    --ink: #555;
    --edge: rgba(0,0,0,0.12);
  }
  * { margin: 0; padding: 0; box-sizing: border-box; }
  html, body { width: 1200px; height: 1041px; overflow: hidden; background: var(--backdrop); }
  body { position: relative; font-family: "Montserrat", sans-serif; font-weight: 300; }

  .piece { position: absolute; box-shadow: 0 1px 2px var(--edge); }
  .paper { background: var(--paper); }
  .bar { position: absolute; top: 0; height: 5px; }
  .bar--teal { background: var(--teal); }
  .bar--grey { background: var(--bar-grey); }
  .firm { color: var(--teal); letter-spacing: -0.03em; white-space: nowrap; position: absolute; }
  .small { color: var(--ink); font-size: 5.5px; line-height: 1.25; position: absolute; white-space: nowrap; }

  /* Folder */
  .folder { left: 166px; top: 76px; width: 417px; height: 541px; background: var(--teal); border-radius: 2px; }
  .folder__spine { position: absolute; left: 0; top: 0; bottom: 0; width: 27px; background: var(--teal-dark); border-right: 1px solid rgba(0,0,0,0.15); }
  .folder__spine::after { content: ""; position: absolute; left: 24px; top: 0; bottom: 0; width: 1px; background: rgba(0,0,0,0.12); }
  .folder .firm { color: #fff; font-size: 24px; right: 50px; top: 71px; }
  .folder__url { position: absolute; right: 50px; top: 99px; color: #fff; font-size: 9.5px; letter-spacing: 0.02em; }

  /* Letterhead */
  .letterhead { left: 615px; top: 95px; width: 403px; height: 523px; }
  .letterhead .firm { font-size: 16px; right: 23px; top: 27px; }
  .letterhead .small { right: 23px; top: 50px; text-align: right; }

  /* Envelope front */
  .envelope-front { left: 132px; top: 645px; width: 451px; height: 196px; }
  .envelope-front .firm { font-size: 16px; left: 23px; top: 26px; }
  .envelope-front .small { left: 23px; top: 48px; }

  /* Envelope back */
  .envelope-back { left: 615px; top: 645px; width: 451px; height: 196px; }
  .envelope-back svg { position: absolute; left: 0; top: 0; }
  .envelope-back__url { position: absolute; left: 0; right: 0; top: 25px; text-align: center; color: #fff; font-size: 6px; }
  .envelope-back__url b { font-weight: 600; }

  /* Business cards */
  .card { top: 870px; width: 167px; height: 96px; }
  .card--front { left: 416px; background: var(--teal); }
  .card--front .firm { color: #fff; font-size: 9.5px; left: 0; right: 0; text-align: center; top: 41px; }
  .card--front .card__url { position: absolute; left: 0; right: 0; top: 77px; text-align: center; color: #fff; font-size: 3.5px; opacity: 0.85; }
  .card--back { left: 615px; }
  .card--back .firm { font-size: 9px; left: 11px; top: 16px; }
  .card--back .small { font-size: 4px; left: 11px; top: 64px; }
  .card__name { position: absolute; right: 9px; top: 61px; text-align: right; color: #444; font-size: 7px; letter-spacing: -0.02em; }
  .card__role { display: block; font-size: 3.8px; margin-top: 1px; letter-spacing: 0; }
</style>
</head>
<body>

  <section class="piece folder">
    <div class="folder__spine"></div>
    <div class="firm">VERIDANE LAW LLC</div>
    <div class="folder__url">www.veridane.com</div>
  </section>

  <section class="piece paper letterhead">
    <div class="bar bar--teal" style="left:0;width:229px"></div>
    <div class="bar bar--grey" style="left:233px;width:170px"></div>
    <div class="firm">VERIDANE LAW LLC</div>
    <div class="small">VERIDANE LAW LLC<br>18 Harbor Lane, Suite 300<br>Easton, MA 02375 &nbsp;Tel: 508-555-0142<br>www.veridane.com</div>
  </section>

  <section class="piece paper envelope-front">
    <div class="bar bar--grey" style="left:0;width:171px"></div>
    <div class="bar bar--teal" style="left:176px;width:275px"></div>
    <div class="firm">VERIDANE LAW LLC</div>
    <div class="small">18 Harbor Lane, Suite 300<br>Easton, MA 02375</div>
  </section>

  <section class="piece paper envelope-back">
    <svg width="451" height="70" viewBox="0 0 451 70" aria-hidden="true">
      <path d="M0 0 H451 L437 60 Q435 64 430 64 H22 Q17 64 15 60 Z" fill="var(--teal)"/>
    </svg>
    <div class="envelope-back__url">www.<b>veridane</b>.com</div>
  </section>

  <section class="piece card card--front">
    <div class="firm">VERIDANE LAW LLC</div>
    <div class="card__url">www.veridane.com</div>
  </section>

  <section class="piece paper card card--back">
    <div class="bar bar--grey" style="left:0;width:90px;height:3px"></div>
    <div class="bar bar--teal" style="left:94px;width:73px;height:3px"></div>
    <div class="firm">VERIDANE LAW LLC</div>
    <div class="small">VERIDANE LAW LLC<br>18 Harbor Lane, Suite 300<br>Easton, MA 02375 &nbsp;Tel: 508-555-0142<br>www.veridane.com</div>
    <div class="card__name">JORDAN ELLERY<span class="card__role">General Manager</span></div>
  </section>

</body>
</html>
```